Business Card Design

Just looking for a good designs that looks good with our company logo. I'd like it to be simple and to the point. Just including contact information, our logo, and my name somewhere on the card so future clients know who they're contacting, and a couple services offered. The two images I attached are pictures of our logo. I don't care which color they they are, I just attached both images to give a reference of logo colors depending on the color of the card.
Names: Calvin Prewitt
Phone: 555-247-9061
Email: tidyturfcrew@mailvista.net
Services offered:
Mowing
Fertilization
Aeration
Bed & tree maintenance
and more.
Industry/Entity Type
Business
Contact Information for Business Card
Names: Calvin Prewitt
Phone: 555-247-9061
Look and feel

```html
<!DOCTYPE html>
<html lang="en">
<head>
<meta charset="UTF-8">
<title>Tidy Turf Crew — Business Card</title>
<link href="https://fonts.googleapis.com/css2?family=Questrial&display=swap" rel="stylesheet">
<style>
  :root {
    --card-bg: #ffffff;
    --ink: #1a1a1a;
    --brand-navy: #1f2a44;
    --brand-red: #e32b2b;
    --bullet-ring: #f7b5b5;
  }
  * { margin: 0; padding: 0; box-sizing: border-box; }
  html, body {
    width: 1200px;
    height: 694px;
    overflow: hidden;
    background: var(--card-bg);
  }
  .card {
    position: relative;
    width: 1200px;
    height: 694px;
    background: var(--card-bg);
    font-family: "Questrial", "Century Gothic", sans-serif;
    color: var(--ink);
  }
  .brand {
    position: absolute;
    left: 170px;
    top: 150px;
    display: flex;
    align-items: center;
    gap: 18px;
  }
  .brand-dot {
    width: 40px;
    height: 40px;
    border-radius: 50%;
    background: var(--brand-red);
    flex: none;
  }
  .brand-name {
    font-size: 40px;
    line-height: 1.1;
    color: var(--brand-navy);
    width: 220px;
  }
  .contact {
    position: absolute;
    left: 0;
    top: 0;
  }
  .contact-name {
    position: absolute;
    left: 498px;
    top: 134px;
    font-size: 44px;
    letter-spacing: 4px;
    white-space: nowrap;
  }
  .contact-name .initial { font-size: 52px; }
  .contact-phone {
    position: absolute;
    left: 596px;
    top: 194px;
    font-size: 31px;
    letter-spacing: 4px;
    white-space: nowrap;
  }
  .contact-email {
    position: absolute;
    left: 500px;
    top: 234px;
    font-size: 33px;
    white-space: nowrap;
  }
  .services-title {
    position: absolute;
    left: 0;
    width: 1198px;
    top: 374px;
    text-align: center;
    font-size: 42px;
    font-weight: normal;
  }
  .services-title span {
    border-bottom: 3px solid var(--ink);
    padding-bottom: 2px;
  }
  .service {
    position: absolute;
    font-size: 45px;
    line-height: 1;
    white-space: nowrap;
    transform: translateY(-50%);
    display: flex;
    align-items: center;
  }
  .service::before {
    content: "";
    display: inline-block;
    width: 14px;
    height: 14px;
    border-radius: 50%;
    background: var(--brand-red);
    box-shadow: 0 0 0 5px var(--bullet-ring);
    margin-right: 22px;
    flex: none;
  }
  .service-mowing { left: 198px; top: 502px; }
  .service-fertilization { left: 481px; top: 502px; }
  .service-aeration { left: 841px; top: 502px; }
  .service-beds { left: 233px; top: 567px; }
</style>
</head>
<body>
  <main class="card">
    <div class="brand">
      <span class="brand-dot"></span>
      <span class="brand-name">Tidy Turf Crew</span>
    </div>

    <div class="contact">
      <p class="contact-name"><span class="initial">C</span>alvin <span class="initial">P</span>rewitt</p>
      <p class="contact-phone">555-247-9061</p>
      <p class="contact-email">tidyturfcrew@mailvista.net</p>
    </div>

    <h2 class="services-title"><span>Services Offered</span></h2>
    <p class="service service-mowing">Mowing</p>
    <p class="service service-fertilization">Fertilization</p>
    <p class="service service-aeration">Aeration</p>
    <p class="service service-beds">Bed &amp; tree maintenance and more</p>
  </main>
</body>
</html>
```